Velora Aesthetica

Medical doctor providing aesthetic medicine

* Double sided card
* Logo to be on card
Other details:
* Dr. Mirela Kostvan, BSc, MBChB, CCFP
* #214-215, 27903 83 Ave, Surrey, BC, V2T 4K7
* 604-718-2943
* info@veloraclinic.ca
* www.veloraclinic.ca

Industry/Entity Type

Medical / Health & Beauty

Contact Information for Business Card

see 'Project Description'

Colors
0054AA
0677BA
7BADD7
CADEEF
E8F1F8
FFF300
FFF600
FEFA6F
FFFEC7
FFFEE8

Requirements
Must have
• Modern, high-end design

```html
<!DOCTYPE html>
<html lang="en">
<head>
<meta charset="utf-8">
<title>Velora Aesthetica – Business Card</title>
<link href="https://fonts.googleapis.com/css2?family=Montserrat:wght@400;500&display=swap" rel="stylesheet">
<style>
  :root {
    --backdrop: #808080;
    --navy: #364d66;
    --gold: #d1ac3a;
    --white: #ffffff;
    --ink: #1d1d1f;
  }
  * { margin: 0; padding: 0; box-sizing: border-box; }
  html, body { width: 1140px; height: 1200px; overflow: hidden; }
  body {
    background: var(--backdrop);
    font-family: "Montserrat", Arial, sans-serif;
    position: relative;
  }
  .card {
    position: absolute;
    left: 223px;
    width: 695px;
    height: 406px;
    overflow: hidden;
  }
  .card--front { top: 135px; background: var(--navy); }
  .card--back { top: 660px; background: var(--white); }

  .brand {
    position: absolute;
    text-align: center;
    transform: translateX(-50%);
    white-space: nowrap;
  }
  .brand__dot {
    display: block;
    margin: 0 auto;
    border: 2px solid var(--gold);
    border-radius: 50%;
  }
  .brand__name { display: block; font-weight: 400; }
  .brand__sub { display: block; font-weight: 500; color: var(--gold); }

  .card--front .brand { left: 186px; top: 108px; }
  .card--front .brand__dot { width: 70px; height: 70px; margin-bottom: 34px; }
  .card--front .brand__name {
    color: var(--white); font-size: 36px; letter-spacing: 12px; padding-left: 12px; line-height: 1;
  }
  .card--front .brand__sub {
    font-size: 11px; letter-spacing: 7.5px; padding-left: 7.5px; margin-top: 10px;
  }

  .card--back .brand { left: 153px; top: 140px; }
  .card--back .brand__dot { width: 54px; height: 54px; margin-bottom: 30px; }
  .card--back .brand__name {
    color: var(--ink); font-size: 22px; letter-spacing: 7px; padding-left: 7px; line-height: 1;
  }
  .card--back .brand__sub {
    font-size: 7.5px; letter-spacing: 4.6px; padding-left: 4.6px; margin-top: 6px;
  }

  .name-band {
    position: absolute;
    left: 299px; right: 0; top: 74px; height: 76px;
    background: var(--navy);
    color: var(--white);
    padding: 10px 0 0 37px;
  }
  .name-band__name { font-size: 28px; font-weight: 400; line-height: 1.05; }
  .name-band__creds { font-size: 14.5px; font-weight: 500; line-height: 1.1; }

  .contact {
    position: absolute;
    left: 301px; top: 188px;
    color: var(--ink);
    font-size: 15px;
    list-style: none;
  }
  .contact__address { margin-bottom: 15px; }
  .contact__item {
    display: flex; align-items: center;
    height: 29.5px;
  }
  .contact__icon { width: 17px; height: 17px; margin-right: 17px; flex: none; }
</style>
</head>
<body>

<section class="card card--front">
  <div class="brand">
    <span class="brand__dot"></span>
    <span class="brand__name">VELORA</span>
    <span class="brand__sub">AESTHETICA</span>
  </div>
</section>

<section class="card card--back">
  <div class="brand">
    <span class="brand__dot"></span>
    <span class="brand__name">VELORA</span>
    <span class="brand__sub">AESTHETICA</span>
  </div>

  <div class="name-band">
    <h1 class="name-band__name">Dr. Mirela Kostvan</h1>
    <p class="name-band__creds">BSc, MBChB, CCFP</p>
  </div>

  <ul class="contact">
    <li class="contact__address">83 Ave, Surrey, BC, V2T 4K7</li>
    <li class="contact__item">
      <svg class="contact__icon" viewBox="0 0 20 20"><circle cx="10" cy="10" r="10" fill="#364d66"/><path d="M7 5.5c.6-.3 1 0 1.3.6l.6 1.3c.2.5 0 .9-.4 1.2l-.4.3c.4 1.1 1.3 2 2.4 2.5l.3-.4c.3-.4.8-.5 1.2-.3l1.3.6c.6.3.8.8.5 1.3-.5.9-1.3 1.4-2.3 1.1C8.8 13.2 6.8 11.2 6 8.5c-.3-1.1.2-2.4 1-3z" fill="#fff"/></svg>
      214-215-27903
    </li>
    <li class="contact__item">
      <svg class="contact__icon" viewBox="0 0 20 20"><circle cx="10" cy="10" r="10" fill="#364d66"/><rect x="7" y="5" width="6" height="10" rx="1.2" fill="none" stroke="#fff" stroke-width="1.4"/><circle cx="10" cy="13" r=".8" fill="#fff"/></svg>
      604-718-2943
    </li>
    <li class="contact__item">
      <svg class="contact__icon" viewBox="0 0 20 20"><circle cx="10" cy="10" r="10" fill="#364d66"/><rect x="5.5" y="7" width="9" height="6.5" fill="#fff"/><path d="M5.5 7l4.5 3.6L14.5 7" fill="none" stroke="#364d66" stroke-width="1"/></svg>
      info@veloraclinic.ca
    </li>
    <li class="contact__item">
      <svg class="contact__icon" viewBox="0 0 20 20"><circle cx="10" cy="10" r="10" fill="#364d66"/><path d="M8 5.5v8.5l2-2 1.4 3 1.2-.6-1.4-2.9 2.8-.2z" fill="#fff"/></svg>
      www.veloraclinic.ca
    </li>
  </ul>
</section>

</body>
</html>
```